Tail Wags Corner

We need a sign design for our new Pet store in Dublin Ireland
The sign has also room for a banner underneath the sign which we feel should show the basic categories of animals we cater for.
Aquatic,Bird,Cat,Dog, small animal and reptile.
I would like these categories in a similar design to Tablix app for example in bright colours with maybe silhouette of animal inside.
We would then incorporate these individual APPs within the category inside the store
the shop name should be blend well the idea above but Tail Wag Corner should not be complicated I feel
70% female and children
Store

```html
<!DOCTYPE html>
<html lang="en">
<head>
<meta charset="utf-8">
<title>Tail Wag Corner – Store Sign</title>
<link rel="stylesheet" href="https://fonts.googleapis.com/css2?family=Fredoka:wght@600&family=Sniglet:wght@800&display=swap">
<style>
  :root {
    --forest: #0f4000;
    --forest-edge: #1d5a0c;
    --walnut: #3a0f02;
    --walnut-edge: #2a0a00;
    --lemon: #ffff66;
    --white: #ffffff;
    --ink: #111111;
    --tile-green: #2f8a1f;
    --tile-blue: #2a3fd6;
    --tile-red: #e0392a;
    --tile-yellow: #f2d51e;
    --tile-purple: #8e1a94;
    --tile-grey: #7a7a7a;
  }
  * { box-sizing: border-box; margin: 0; padding: 0; }
  html, body { width: 1200px; height: 732px; overflow: hidden; background: var(--white); }
  .canvas { position: relative; width: 1200px; height: 732px; }

  .sign, .banner { position: absolute; display: flex; align-items: center; justify-content: center; }
  .sign::before, .banner::before {
    content: ""; position: absolute; border: 2px solid var(--white); pointer-events: none;
  }
  .sign::before { inset: 13px; }
  .banner::before { inset: 4px; border-width: 1.5px; }

  .sign--green { left: 0; top: 0; width: 1200px; height: 192px; background: var(--forest); }
  .sign--brown { left: 5px; top: 415px; width: 1192px; height: 193px; background: var(--walnut); }

  .sign__name { position: relative; line-height: 1; white-space: nowrap; paint-order: stroke fill; }
  .sign--green .sign__name {
    font-family: "Fredoka", sans-serif; font-weight: 600; font-size: 118px;
    color: var(--lemon); -webkit-text-stroke: 5px var(--ink);
  }
  .sign--brown .sign__name {
    font-family: "Sniglet", sans-serif; font-weight: 800; font-size: 112px; letter-spacing: 2px;
    color: var(--white); -webkit-text-stroke: 6px var(--ink);
  }

  .banner { gap: 6px; padding: 0 14px; justify-content: space-between; }
  .banner--green { left: 145px; top: 255px; width: 871px; height: 60px; background: var(--forest); border: 3px solid var(--forest-edge); }
  .banner--brown { left: 152px; top: 671px; width: 868px; height: 59px; background: var(--walnut); border: 3px solid var(--walnut-edge); }

  .banner__tiles { display: flex; gap: 7px; position: relative; }
  .tile {
    width: 39px; height: 39px; border-radius: 6px; border: 2px solid rgba(255,255,255,0.85);
    box-shadow: inset 0 -6px 8px rgba(0,0,0,0.25);
  }
  .tile--aquatic { background: linear-gradient(160deg, #6bd35a, var(--tile-green)); }
  .tile--bird { background: linear-gradient(160deg, #6f84ff, var(--tile-blue)); }
  .tile--cat { background: linear-gradient(160deg, #ff7a66, var(--tile-red)); }
  .tile--dog { background: linear-gradient(160deg, #fff176, var(--tile-yellow)); }
  .tile--small { background: linear-gradient(160deg, #c64fcc, var(--tile-purple)); }
  .tile--reptile { background: linear-gradient(160deg, #b0b0b0, var(--tile-grey)); }

  .banner__tagline { position: relative; white-space: nowrap; line-height: 1; paint-order: stroke fill; }
  .banner--green .banner__tagline {
    font-family: "Fredoka", sans-serif; font-weight: 600; font-size: 37px;
    color: var(--lemon); -webkit-text-stroke: 2px var(--ink);
  }
  .banner--brown .banner__tagline {
    font-family: "Sniglet", sans-serif; font-weight: 800; font-size: 37px; letter-spacing: 1px;
    color: var(--white); -webkit-text-stroke: 3px var(--ink);
  }
</style>
</head>
<body>
<main class="canvas">
  <section class="sign sign--green">
    <h1 class="sign__name">Tail Wag Corner</h1>
  </section>
  <section class="banner banner--green">
    <div class="banner__tiles">
      <div class="tile tile--aquatic" role="img" aria-label="Aquatic category tile with fish silhouette"></div>
      <div class="tile tile--bird" role="img" aria-label="Bird category tile with bird silhouette"></div>
      <div class="tile tile--cat" role="img" aria-label="Cat category tile with cat silhouette"></div>
    </div>
    <p class="banner__tagline">For all your pet needs</p>
    <div class="banner__tiles">
      <div class="tile tile--dog" role="img" aria-label="Dog category tile with dog silhouette"></div>
      <div class="tile tile--small" role="img" aria-label="Small animal category tile with rabbit silhouette"></div>
      <div class="tile tile--reptile" role="img" aria-label="Reptile category tile with snake silhouette"></div>
    </div>
  </section>

  <section class="sign sign--brown">
    <h2 class="sign__name">Tail Wag Corner</h2>
  </section>
  <section class="banner banner--brown">
    <div class="banner__tiles">
      <div class="tile tile--aquatic" role="img" aria-label="Aquatic category tile with fish silhouette"></div>
      <div class="tile tile--bird" role="img" aria-label="Bird category tile with bird silhouette"></div>
      <div class="tile tile--cat" role="img" aria-label="Cat category tile with cat silhouette"></div>
    </div>
    <p class="banner__tagline">For all your pet needs</p>
    <div class="banner__tiles">
      <div class="tile tile--dog" role="img" aria-label="Dog category tile with dog silhouette"></div>
      <div class="tile tile--small" role="img" aria-label="Small animal category tile with rabbit silhouette"></div>
      <div class="tile tile--reptile" role="img" aria-label="Reptile category tile with snake silhouette"></div>
    </div>
  </section>
</main>
</body>
</html>
```